依頼詳細
A社より添付の案を頂いているのですが、①グループ会社である安心感親近感をアピールしたい②メリット1のA社専用のプランを他のメリットよりも強調したいと思い、依頼をさせて頂く事となりました。
注意点、会社案内欄の箇所は空白でお願い致します。
社名を変更して今後活用したいので、パワーポイントでの納品をお願い致します。
記載項目
株式会社ZAT/03-4817-2935/https://www.za-t.jp/
サイズ
A4
ページ数
片面
希望イメージ
シンプル 複雑
単色 カラフル
暗い 明るい
日常 高級
遊び心 厳粛
未来的 伝統的
女性的 男性的
希望する色
納品ファイル
補足説明
■ 選んだ理由

社員の選定を元に選ばせて頂きました。親近感があるという意見が多かったです。

■ 提案者全員のお礼・コメント

締め切りが近い中多数のご応募頂きありがとうございます。またご機会ありましたら宜しくお願い致します。

```html
<!DOCTYPE html>
<html lang="ja">
<head>
<meta charset="utf-8">
<title>火災保険 提携代理店のご紹介</title>
<link href="https://fonts.googleapis.com/css2?family=Noto+Sans+JP:wght@400;500;700;900&display=swap" rel="stylesheet">
<style>
:root{
  --navy:#1d2c6a;
  --navy-dark:#14204f;
  --gold:#c6a04c;
  --gold-light:#e6cf8f;
  --accent:#e2532a;
  --ink:#333;
  --muted:#888;
  --line:#d6d9e4;
  --paper:#ffffff;
  --tint:#f3f4f8;
}
*{box-sizing:border-box;margin:0;padding:0}
html,body{width:848px;height:1200px;overflow:hidden;background:var(--paper)}
body{font-family:"Noto Sans JP",sans-serif;color:var(--ink);position:relative}
.period-tag{position:absolute;top:10px;right:24px;background:var(--navy);color:#fff;font-size:10px;padding:2px 8px}
.headline{position:absolute;top:34px;left:0;width:100%;text-align:center;color:var(--navy);font-weight:900;font-size:36px;letter-spacing:1px}
.subhead{position:absolute;top:90px;left:0;width:100%;text-align:center;color:var(--navy);font-weight:700;font-size:20px}
.relation{position:absolute;top:120px;left:0;width:100%;text-align:center;color:var(--navy);font-weight:500;font-size:15px}
.relation:before,.relation:after{content:"";display:inline-block;width:140px;height:1px;background:var(--gold);vertical-align:middle;margin:0 14px}
.intro-band{position:absolute;top:152px;left:0;width:100%;height:100px;background:var(--navy);color:#fff}
.intro-band .from{position:absolute;top:14px;left:0;width:100%;text-align:center;font-size:22px;font-weight:700}
.intro-band .from .box{display:inline-block;background:#fff;color:var(--navy);padding:0 10px;margin:0 4px;font-size:24px}
.intro-band .plan{position:absolute;top:50px;left:0;width:100%;text-align:center;font-size:30px;font-weight:900}
.intro-band .plan em{font-style:normal;color:var(--gold-light)}
.intro-band:after{content:"";position:absolute;bottom:-5px;left:0;width:100%;height:3px;background:var(--gold)}
.merit-pair{position:absolute;top:268px;left:24px;width:800px;display:flex;gap:16px}
.merit-card{flex:1;height:272px;border:2px solid var(--navy);background:#fff;position:relative}
.merit-card.primary{border-color:var(--accent);border-width:3px}
.merit-badge{position:absolute;top:-8px;left:10px;width:56px;height:62px}
.merit-head{height:40px;background:linear-gradient(90deg,var(--gold),var(--gold-light));color:var(--navy);font-weight:900;font-size:17px;line-height:40px;padding-left:80px}
.merit-body{display:flex;padding:18px 14px 0 14px;gap:12px}
.icon-slot{width:78px;height:78px;flex:none;border-radius:50%;background:var(--tint)}
.merit-title{font-size:22px;font-weight:900;color:var(--navy);line-height:1.35}
.merit-title .hl{color:var(--accent);font-size:25px}
.merit-title .mark{background:linear-gradient(transparent 60%,var(--gold-light) 60%)}
.merit-text{padding:14px 18px 0;font-size:13px;line-height:1.7}
.merit-text b{color:var(--accent)}
.merit-row{position:absolute;left:24px;width:800px;border:2px solid var(--navy);background:#fff;display:flex;align-items:center}
.merit-row .merit-badge{position:static;margin:0 14px 0 10px;flex:none}
.row-3{top:556px;height:118px}
.row-4{top:686px;height:72px}
.row-5{top:770px;height:72px}
.row-title{font-size:21px;font-weight:900;color:var(--navy)}
.row-title .hl{color:var(--accent)}
.row-note{font-size:11px;color:var(--ink);margin-top:4px}
.row-icon{width:54px;height:54px;background:var(--tint);border-radius:6px;flex:none;margin-right:14px}
.stats{display:flex;gap:14px;margin-top:8px}
.stat{border:1px solid var(--line);background:var(--tint);padding:3px 10px;font-size:10px;text-align:center;width:170px}
.stat strong{display:block;font-size:18px;color:var(--accent);font-weight:900}
.info-area{position:absolute;top:858px;left:24px;width:800px;height:320px;border-top:1px solid var(--line)}
.info-area .label{position:absolute;bottom:12px;width:100%;text-align:center;font-size:12px;color:var(--muted)}
</style>
</head>
<body>
<div class="period-tag">2021年1月以降保険期間用</div>
<h1 class="headline">○○○○○の住宅をご購入されるお客さまへ</h1>
<p class="subhead">火災保険 提携代理店のご紹介</p>
<p class="relation">□□□□□は、○○○○○のグループ会社です。</p>

<section class="intro-band">
  <p class="from">グループ会社<span class="box">□□□□□</span>から、</p>
  <p class="plan">○○○○○専用 <em>火災保険</em>のご案内です。</p>
</section>

<div class="merit-pair">
  <article class="merit-card primary">
    <svg class="merit-badge" viewBox="0 0 56 62"><polygon points="28,0 56,22 56,62 0,62 0,22" fill="#1d2c6a"/><text x="28" y="33" fill="#fff" font-size="9" text-anchor="middle" font-family="Noto Sans JP,sans-serif">merit</text><text x="28" y="55" fill="#fff" font-size="20" font-weight="700" text-anchor="middle" font-family="Noto Sans JP,sans-serif">1</text></svg>
    <div class="merit-head">グループ会社ならでは！</div>
    <div class="merit-body">
      <div class="icon-slot" role="img" aria-label="住宅のイラスト"></div>
      <p class="merit-title">○○○○○オーナーさま<br><span class="hl mark">専用プラン適用!</span></p>
    </div>
    <p class="merit-text">グループ会社ですので、<br><b>割安な保険料</b>（地震保険は除く）<br>でご契約いただけます。</p>
  </article>
  <article class="merit-card">
    <svg class="merit-badge" viewBox="0 0 56 62"><polygon points="28,0 56,22 56,62 0,62 0,22" fill="#1d2c6a"/><text x="28" y="33" fill="#fff" font-size="9" text-anchor="middle" font-family="Noto Sans JP,sans-serif">merit</text><text x="28" y="55" fill="#fff" font-size="20" font-weight="700" text-anchor="middle" font-family="Noto Sans JP,sans-serif">2</text></svg>
    <div class="merit-head">グループ会社ならでは！</div>
    <div class="merit-body">
      <div class="icon-slot" role="img" aria-label="書類のイラスト"></div>
      <p class="merit-title">お建物資料等の<br><span class="hl">ご提出不要!</span></p>
    </div>
    <p class="merit-text">グループ会社ですので、<br>○○○○○と□□□□□で<br>直接やりとりいたしますので、<br>お客さまのお手間を省けます。</p>
  </article>
</div>

<section class="merit-row row-3">
  <svg class="merit-badge" viewBox="0 0 56 62" width="56" height="62"><polygon points="28,0 56,22 56,62 0,62 0,22" fill="#1d2c6a"/><text x="28" y="33" fill="#fff" font-size="9" text-anchor="middle" font-family="Noto Sans JP,sans-serif">merit</text><text x="28" y="55" fill="#fff" font-size="20" font-weight="700" text-anchor="middle" font-family="Noto Sans JP,sans-serif">3</text></svg>
  <div>
    <p class="row-title">□□□□□は<span class="hl">火災保険専門代理店</span>です!</p>
    <p class="row-note">火災保険専門ですのでお客さまにわかりやすくご案内いたします。</p>
    <div class="stats">
      <div class="stat">2019年度火災保険取扱件数<strong>約3,500件</strong></div>
      <div class="stat">2020年8月時点保険契約件数<strong>約28,000件</strong></div>
    </div>
  </div>
</section>

<section class="merit-row row-4">
  <svg class="merit-badge" viewBox="0 0 56 62" width="50" height="56"><polygon points="28,0 56,22 56,62 0,62 0,22" fill="#1d2c6a"/><text x="28" y="33" fill="#fff" font-size="9" text-anchor="middle" font-family="Noto Sans JP,sans-serif">merit</text><text x="28" y="55" fill="#fff" font-size="20" font-weight="700" text-anchor="middle" font-family="Noto Sans JP,sans-serif">4</text></svg>
  <div class="row-icon" role="img" aria-label="カレンダーのイラスト"></div>
  <div>
    <p class="row-title"><span class="hl">土日祝日も</span>ご案内いたします!</p>
    <p class="row-note">お客さまのご都合のよい日時にご案内いたします。</p>
  </div>
</section>

<section class="merit-row row-5">
  <svg class="merit-badge" viewBox="0 0 56 62" width="50" height="56"><polygon points="28,0 56,22 56,62 0,62 0,22" fill="#1d2c6a"/><text x="28" y="33" fill="#fff" font-size="9" text-anchor="middle" font-family="Noto Sans JP,sans-serif">merit</text><text x="28" y="55" fill="#fff" font-size="20" font-weight="700" text-anchor="middle" font-family="Noto Sans JP,sans-serif">5</text></svg>
  <div class="row-icon" role="img" aria-label="ロケットのイラスト"></div>
  <div>
    <p class="row-title"><span class="hl">スピーディー</span>なお申込手続き!</p>
    <p class="row-note">最短で当日から補償開始のお手続きが可能です。</p>
  </div>
</section>

<div class="info-area"><p class="label">注意点・会社案内欄</p></div>
</body>
</html>
```